Business Card Design Project

We would need a business name card for our online website business, http://www.brindle.com.sg/. We would need to include our website on the name card as well.

Target Market(s)

Adults and kids in Singapore, mainly expatriates

Industry/Entity Type

Business

Font styles to use
Sans Serif

Colors

Designer to choose colors to be used in the design.

Requirements
Must have
• Must include our "vorn" logo and we would like our name card to be printed on light craft paper material

```html
<!DOCTYPE html>
<html lang="en">
<head>
<meta charset="utf-8">
<title>vorn business card</title>
<link href="https://fonts.googleapis.com/css2?family=Roboto:wght@300;400;500&display=swap" rel="stylesheet">
<style>
  :root {
    --backdrop: #e9e6e1;
    --card: #ffffff;
    --brand-blue: #3d55a5;
    --brand-red: #e0394f;
    --ink: #2b2b2b;
    --rule: #333333;
    --shadow: rgba(60, 45, 25, 0.22);
  }
  * { box-sizing: border-box; margin: 0; padding: 0; }
  html, body {
    width: 1200px; height: 858px; overflow: hidden;
    background: var(--backdrop);
    font-family: "Roboto", Arial, sans-serif;
  }
  .stage { position: relative; width: 1200px; height: 858px; }
  .card {
    position: absolute;
    width: 540px; height: 310px;
    background: var(--card);
    box-shadow: 0 10px 28px var(--shadow), 0 2px 4px var(--shadow);
  }
  .card--front { left: 60px; top: 90px; display: flex; }
  .card--back { left: 600px; top: 458px; }

  .brand {
    display: flex; align-items: center; gap: 14px;
    color: var(--brand-blue); font-weight: 500; letter-spacing: 1px;
  }
  .brand__dot { border-radius: 50%; background: var(--brand-red); flex: none; }

  .front__logo {
    width: 240px; display: flex; align-items: center; justify-content: center;
  }
  .front__logo .brand { font-size: 54px; }
  .front__logo .brand__dot { width: 30px; height: 30px; }
  .front__divider { width: 1px; background: var(--rule); margin: 40px 0; }
  .front__info { flex: 1; padding: 52px 0 0 40px; }
  .person__name { color: var(--brand-blue); font-size: 26px; font-weight: 400; }
  .person__title { color: var(--brand-red); font-size: 13px; font-weight: 300; margin-top: 3px; }
  .contacts { list-style: none; margin-top: 30px; }
  .contacts li {
    display: flex; align-items: center; gap: 12px;
    font-size: 15px; font-weight: 300; color: var(--brand-blue);
    margin-bottom: 13px;
  }
  .contacts svg { width: 22px; height: 22px; flex: none; }

  .back__logo {
    position: absolute; left: 0; right: 0; top: 100px;
    display: flex; justify-content: center;
  }
  .back__logo .brand { font-size: 66px; }
  .back__logo .brand__dot { width: 38px; height: 38px; }
  .back__tagline {
    position: absolute; left: 32px; bottom: 26px;
    color: var(--brand-blue); font-size: 19px; font-weight: 300;
  }
</style>
</head>
<body>
<div class="stage">
  <section class="card card--front">
    <div class="front__logo">
      <div class="brand"><span class="brand__dot"></span><span class="brand__name">vorn</span></div>
    </div>
    <div class="front__divider"></div>
    <div class="front__info">
      <h1 class="person__name">Employee Name</h1>
      <p class="person__title">Managing Director</p>
      <ul class="contacts">
        <li>
          <svg viewBox="0 0 22 22"><circle cx="11" cy="11" r="9.5" fill="none" stroke="var(--brand-blue)" stroke-width="2"/><path d="M8 7c-1 1 0 4 2 6s5 3 6 2l-1.5-1.8-1.5.8c-1-.5-2.5-2-3-3l.8-1.5z" fill="var(--brand-red)"/></svg>
          (+65) 61004280
        </li>
        <li>
          <svg viewBox="0 0 22 22"><circle cx="11" cy="11" r="9.5" fill="none" stroke="var(--brand-blue)" stroke-width="2"/><rect x="6.5" y="9" width="9" height="6" rx="1" fill="var(--brand-red)"/><rect x="8.5" y="6.5" width="5" height="3" fill="var(--brand-red)"/></svg>
          (+65) 61004287
        </li>
        <li>
          <svg viewBox="0 0 22 22"><circle cx="11" cy="11" r="9.5" fill="none" stroke="var(--brand-blue)" stroke-width="2"/><rect x="6" y="7.5" width="10" height="7" fill="var(--brand-red)"/><path d="M6 7.5l5 4 5-4" fill="none" stroke="#fff" stroke-width="1"/></svg>
          email@vorncorp.com
        </li>
        <li>
          <svg viewBox="0 0 22 22"><circle cx="11" cy="11" r="9.5" fill="none" stroke="var(--brand-blue)" stroke-width="2"/><circle cx="11" cy="11" r="5" fill="var(--brand-red)"/><path d="M6 11h10M11 6v10" stroke="#fff" stroke-width="0.8"/></svg>
          www.brindle.com.sg
        </li>
      </ul>
    </div>
  </section>

  <section class="card card--back">
    <div class="back__logo">
      <div class="brand"><span class="brand__dot"></span><span class="brand__name">vorn</span></div>
    </div>
    <p class="back__tagline">chocolates, candies, snacks &amp; drinks lovers!</p>
  </section>
</div>
</body>
</html>
```